Guaranteed Job - Sleek Sexy Business Card UV Spot

Im looking for a sleek and sexy business card, that resembles elite or VIP status status.
our business is corinvale.example
you can view our products on there, but our main audience for handing out our cards will be for people in the hospitality industry, so it will need to impress high management and CEO of hotels and restaurants, bars, clubs etc...
the card features will have UV spot on both sides, 400gsm stock. standard size.
Artwork should be 86 x 54mm + 2mm bleed = 90 x 58mm
it should have a nice "unique" uv spot pattern that highlights the card, not a repeated pattern, theres no originality there, and it will be disregarded.
The written material will be:
Corin Vale Hospitality College (logo)
Tobin Marsh
Director
Phone: 1300 615 737
Mobile: 0455 817 296
Email: info@corinvale.example
website: www.corinvale.example
I'm looking for originality here, i don't want just a simple stock card, want something that has a wow factor for people.
You will find the logo attached. you may invert the white to black words to suit the background as you please.
thank you and good luck
As a side note, ive received a lot of proposals, im too busy to give feedback to each and every one, so if i havent provided feedback for your design within 24 hours, then consider it not acceptable, and you could resubmit another design.
So far i have not seen any design that stood out for me, they all seem pretty generic. there nothing thats unique, i would figure for the amount that im offering, that people would put some more effort and creativity into the design.
so far over 200 designs submitted, and nothing i have seen looks very original, everything looks like a different variation of the same stuff, i said it very clearly i wanted something unique, the only thing that has come close to it so far is this one
Reason: Ive received alot of design concepts and i have reviewed everyone, but i havent had time to give feedback to every single one, only the ones that have interested me, if i havent responded, its because i havent found it good enough.
so far only a few design have been on par with what ive been looking for, an attractive eye popping design.
heres a few of them,
http://files.pixelbazaar.example/design_img/51736/62418/62418_2840915_51736_image.jpg
http://files.pixelbazaar.example/design_img/51736/68254/68254_2841377_51736_image.jpg
theyre, both unique and original, and eye catching, the only thing theyre missing is the sexyness.
if you still think you have some creativity left in your minds, then throw it on here.
Reason: Sorry guys for the delay, I was in a serious accident and out of commission for the past few months, I'm just slowly recovering now, please bare with me as i try to attend to this project, it may take me awhile as I have other projects that are on standby, I'm not 100% at the moment, so im extending the deadline for 2 weeks right now. Thanks for your patience.
Hospitality

```html
<!DOCTYPE html>
<html lang="en">
<head>
<meta charset="utf-8">
<title>Corin Vale Hospitality College – Business Card</title>
<link rel="stylesheet" href="https://fonts.googleapis.com/css2?family=Barlow+Semi+Condensed:wght@500;600;700&family=Exo+2:ital,wght@1,800&display=swap">
<style>
  :root {
    --backdrop: #d9d6d2;
    --card-white: #f4f4f3;
    --card-black: #2a2a2a;
    --card-black-edge: #1e1e1e;
    --ink-dark: #1c1c1c;
    --ink-grey: #6f6f6f;
    --ink-white: #f5f5f5;
    --accent-blue: #4aa6d8;
    --circle-dark: #2d2d2d;
  }
  * { margin: 0; padding: 0; box-sizing: border-box; }
  html, body {
    width: 1200px;
    height: 1000px;
    overflow: hidden;
    background: var(--backdrop);
  }
  .sheet {
    width: 1200px;
    height: 1000px;
    display: flex;
    flex-direction: column;
    align-items: center;
    justify-content: center;
    gap: 34px;
  }
  .card {
    width: 744px;
    height: 467px;
    position: relative;
    overflow: hidden;
    box-shadow: 0 10px 28px rgba(0,0,0,0.25);
  }

  /* Back: contact side */
  .card--contact {
    background: var(--card-white);
  }
  .holder {
    position: absolute;
    left: 40px;
    top: 200px;
    font-family: "Exo 2", sans-serif;
    color: var(--ink-dark);
    text-transform: uppercase;
    white-space: nowrap;
  }
  .holder__name {
    font-weight: 800;
    font-style: italic;
    font-size: 30px;
    line-height: 1;
    letter-spacing: 0.3px;
  }
  .holder__role {
    font-weight: 800;
    font-style: italic;
    font-size: 15px;
    margin-top: 4px;
  }
  .brand-seal {
    position: absolute;
    left: 268px;
    top: 125px;
    width: 216px;
    height: 216px;
    border-radius: 50%;
    background: var(--circle-dark);
    display: flex;
    align-items: center;
    justify-content: center;
    text-align: center;
  }
  .brand-seal__name {
    font-family: "Barlow Semi Condensed", sans-serif;
    font-weight: 600;
    color: var(--ink-white);
    text-transform: uppercase;
    font-size: 24px;
    line-height: 1.05;
    letter-spacing: 0.5px;
  }
  .contact {
    position: absolute;
    left: 506px;
    top: 185px;
    list-style: none;
    font-family: "Barlow Semi Condensed", sans-serif;
    font-weight: 700;
    font-size: 14px;
    line-height: 1.75;
    color: var(--ink-grey);
    text-transform: uppercase;
    letter-spacing: 0.3px;
    white-space: nowrap;
  }
  .contact__email, .contact__web { text-transform: none; }

  /* Front: brand side */
  .card--brand {
    background: radial-gradient(ellipse at 70% 30%, #363636 0%, var(--card-black) 55%, var(--card-black-edge) 100%);
  }
  .brand-mark {
    position: absolute;
    left: 70px;
    top: 70px;
    width: 327px;
    height: 327px;
    border-radius: 50%;
    background: var(--accent-blue);
  }
  .brand-name {
    position: absolute;
    left: 430px;
    top: 166px;
    font-family: "Barlow Semi Condensed", sans-serif;
    font-weight: 600;
    color: var(--ink-white);
    text-transform: uppercase;
    font-size: 48px;
    line-height: 1;
    letter-spacing: 1px;
  }
  .brand-name span { display: block; }
  .brand-name .brand-name__tail { font-size: 25px; margin-top: 6px; letter-spacing: 0.5px; }
</style>
</head>
<body>
  <main class="sheet">
    <section class="card card--contact" aria-label="Business card, contact side">
      <div class="holder">
        <p class="holder__name">Tobin Marsh</p>
        <p class="holder__role">Director</p>
      </div>
      <div class="brand-seal">
        <p class="brand-seal__name">Corin Vale<br>Hospitality<br>College</p>
      </div>
      <ul class="contact">
        <li>Phone: 1300 615 737</li>
        <li>Mobile: 0455 817 296</li>
        <li>Email: <span class="contact__email">info@corinvale.example</span></li>
        <li>Web: <span class="contact__web">www.corinvale.example</span></li>
      </ul>
    </section>

    <section class="card card--brand" aria-label="Business card, brand side">
      <div class="brand-mark"></div>
      <p class="brand-name">
        <span>Corin Vale</span>
        <span class="brand-name__tail">Hospitality College</span>
      </p>
    </section>
  </main>
</body>
</html>
```